Bramblecourt Homes Stationary
Fast Settlements
Professional
Dorian Pelletier
Managing Member
4817 Larkspur Ave Suite 210
Washington, DC
dgpelletier@bramblecourthomes.net
www.bramblecourthomes.net
Business License # 782645113058
Cash Buyer, Fast Closing.
Residential and Commercial
We are a Nation Wide Buyer.
will upload ai file shortly
vector logo file

```html
<!DOCTYPE html>
<html lang="en">
<head>
<meta charset="utf-8">
<title>Bramblecourt Homes – Business Card</title>
<link href="https://fonts.googleapis.com/css2?family=Michroma&display=swap" rel="stylesheet">
<style>
  :root {
    --backdrop: #e9e7e3;
    --card: #ffffff;
    --brand-green: #1f9a3f;
    --brand-green-dark: #15782f;
    --ink: #3b3b3b;
    --ink-soft: #6d6d6d;
    --rule: #9a9a9a;
  }
  * { box-sizing: border-box; margin: 0; padding: 0; }
  html, body {
    width: 1200px;
    height: 902px;
    overflow: hidden;
    background: var(--backdrop);
    font-family: "Michroma", sans-serif;
  }
  .business-card {
    position: absolute;
    left: 100px;
    top: 165px;
    width: 1000px;
    height: 572px;
    background: var(--card);
    box-shadow: 0 10px 30px rgba(0,0,0,0.18);
    overflow: hidden;
  }
  .web-band {
    position: absolute;
    right: 0;
    top: 0;
    width: 52px;
    height: 100%;
    background: linear-gradient(90deg, var(--brand-green) 0%, var(--brand-green-dark) 100%);
    display: flex;
    align-items: center;
    justify-content: center;
  }
  .web-band__text {
    transform: rotate(90deg);
    white-space: nowrap;
    color: #ffffff;
    font-size: 15px;
    letter-spacing: 1px;
    font-variant: small-caps;
  }
  .brand-block {
    position: absolute;
    left: 70px;
    top: 110px;
    width: 400px;
    text-align: center;
  }
  .brand-mark {
    display: block;
    width: 30px;
    height: 30px;
    margin: 0 auto 16px;
    background: var(--brand-green);
  }
  .brand-name {
    font-size: 32px;
    line-height: 1.2;
    color: var(--brand-green);
    text-transform: uppercase;
    letter-spacing: 1px;
    font-weight: 400;
  }
  .brand-name__sub {
    display: block;
    margin-top: 6px;
    font-size: 20px;
    letter-spacing: 6px;
    color: var(--brand-green-dark);
  }
  .brand-rule {
    width: 330px;
    height: 0;
    border-top: 1.5px dotted var(--rule);
    margin: 14px auto 0;
  }
  .person {
    position: absolute;
    left: 100px;
    top: 282px;
  }
  .person__name {
    font-size: 14px;
    color: var(--brand-green);
    font-variant: small-caps;
    letter-spacing: 0.5px;
  }
  .person__title {
    margin-top: 6px;
    font-size: 12px;
    color: var(--ink-soft);
    font-variant: small-caps;
  }
  .contact-list {
    position: absolute;
    left: 515px;
    top: 230px;
    list-style: none;
  }
  .contact-list__item {
    display: flex;
    align-items: center;
    height: 27px;
    font-size: 13px;
    color: var(--ink);
    font-variant: small-caps;
    white-space: nowrap;
  }
  .contact-list__item--indent { padding-left: 26px; }
  .contact-icon {
    width: 18px;
    height: 18px;
    margin-right: 8px;
    flex: none;
  }
</style>
</head>
<body>
  <main class="business-card">
    <section class="brand-block">
      <span class="brand-mark"></span>
      <h1 class="brand-name">Bramblecourt<span class="brand-name__sub">Homes</span></h1>
      <div class="brand-rule"></div>
    </section>

    <section class="person">
      <p class="person__name">Dorian Pelletier</p>
      <p class="person__title">Managing Member</p>
    </section>

    <ul class="contact-list">
      <li class="contact-list__item">
        <svg class="contact-icon" viewBox="0 0 18 18"><circle cx="9" cy="9" r="9" fill="var(--brand-green)"/><path d="M9 4a3 3 0 0 0-3 3c0 2.3 3 6 3 6s3-3.7 3-6a3 3 0 0 0-3-3z" fill="#fff"/><circle cx="9" cy="7" r="1.1" fill="var(--brand-green)"/></svg>
        4817 Larkspur Ave Suite 210
      </li>
      <li class="contact-list__item contact-list__item--indent">Washington, DC 20090</li>
      <li class="contact-list__item">
        <svg class="contact-icon" viewBox="0 0 18 18"><circle cx="9" cy="9" r="9" fill="var(--brand-green)"/><path d="M6 4.5l2 2-1 1.2c.6 1.3 1.6 2.3 2.9 2.9l1.2-1 2 2-1.3 1.4C8.5 12.6 5.4 9.5 4.6 6z" fill="#fff"/></svg>
        1-800-555-0142
      </li>
      <li class="contact-list__item">
        <svg class="contact-icon" viewBox="0 0 18 18"><circle cx="9" cy="9" r="9" fill="var(--brand-green)"/><rect x="6.2" y="3.8" width="5.6" height="10.4" rx="1" fill="#fff"/><rect x="7.2" y="5" width="3.6" height="6.5" fill="var(--brand-green)"/></svg>
        202-555-0178
      </li>
      <li class="contact-list__item">
        <svg class="contact-icon" viewBox="0 0 18 18"><circle cx="9" cy="9" r="9" fill="var(--brand-green)"/><rect x="4.5" y="7" width="9" height="5.5" rx="0.8" fill="#fff"/><rect x="6" y="4.5" width="6" height="2.5" fill="#fff"/></svg>
        410-555-0123
      </li>
      <li class="contact-list__item">
        <svg class="contact-icon" viewBox="0 0 18 18"><circle cx="9" cy="9" r="9" fill="var(--brand-green)"/><rect x="4.5" y="5.5" width="9" height="7" rx="0.8" fill="#fff"/><path d="M4.8 6l4.2 3.4L13.2 6" stroke="var(--brand-green)" stroke-width="1" fill="none"/></svg>
        dgpelletier@bramblecourthomes.net
      </li>
      <li class="contact-list__item">
        <svg class="contact-icon" viewBox="0 0 18 18"><circle cx="9" cy="9" r="9" fill="var(--brand-green)"/><circle cx="9" cy="9" r="4.5" fill="none" stroke="#fff" stroke-width="1.2"/><path d="M4.5 9h9M9 4.5c-2 2.5-2 6.5 0 9M9 4.5c2 2.5 2 6.5 0 9" stroke="#fff" stroke-width="1" fill="none"/></svg>
        www.bramblecourthomes.net
      </li>
    </ul>

    <aside class="web-band">
      <span class="web-band__text">www.Bramblecourthomes.net</span>
    </aside>
  </main>
</body>
</html>
```